UI/UX design for non-profit education/student success foundation website

Looking to work with a ui/ux designer that can provide an elegant, impactful and modern responsive design for a non-profit education/student success foundation website. The website will need to have a lot of visuals and elements with impactful statements. The responsive templates will later be parsed (this will be done by another developer) and converted to Concrete5 CMS templates. The organization likes bold colors with a modern sleek design. Typography is also key in titles and statements of interest. On-scroll visuals could be nice if it lends well to combining imagery and text. The site will need templates for a homepage, global sub-page, and contact page. Interchangeable block elements would be nice if we want to create other templates or change element positions.

Target Market(s)

Continued education and philanthropy individuals/organizations

Industry/Entity Type

Non-profit / college education

Coding

Coded - Design and coding required

Number of Pages Required

3 page

Font styles to use
Sans Serif
Script

Colors
0094D4
00A9DD
6FCCEA
C7EBF8
E9F6FB
59FF00
82FF00
B8FF75
E3FFCB
F4FFEA
FFC000
F8CF3A
FAE287
FDF2CF
FEFAEE
EE7325
F08F49
F5BC92
FAE3D3
FDF4ED
6B429C
8869AF
B7A5CE
E3DAEB
F3F0F8

Requirements
Must have
• Modern responsive design, impactful visual elements, available theme elements pre styled for things like forms, buttoms, tables...
Nice to have
• Onscroll vidual effects, heros with background video

```html
<!DOCTYPE html>
<html lang="en">
<head>
<meta charset="utf-8">
<title>Kelden Foundation</title>
<link href="https://fonts.googleapis.com/css2?family=Lato:wght@400;700;900&display=swap" rel="stylesheet">
<style>
:root{
  --blue:#1e9ad6;
  --yellow:#fbb41d;
  --orange:#e45c24;
  --purple:rgba(107,66,156,.88);
  --ink:#1f1f1f;
  --body:#3a3a3a;
  --footer:#1c1c1c;
  --footer-text:#a8a8a8;
  --white:#ffffff;
}
*{margin:0;padding:0;box-sizing:border-box}
html,body{width:1200px;height:4465px;overflow:hidden}
body{font-family:'Lato',sans-serif;color:var(--body);background:var(--white);position:relative}
section,header,footer{position:absolute;left:0;width:1200px}
.abs{position:absolute}
.photo{position:absolute}
.btn{position:absolute;display:flex;align-items:center;justify-content:center;background:var(--yellow);color:var(--white);font-weight:700;text-decoration:none;white-space:nowrap}
.btn-lg{font-size:26px}
/* hero */
.hero{top:0;height:760px;background:linear-gradient(100deg,#5b4a3c 0%,#7c6e62 35%,#a4473a 70%,#6d3a34 100%)}
.brand{left:75px;top:90px;font-size:38px;font-weight:700;color:var(--white);white-space:nowrap}
.nav{left:420px;top:100px;display:flex}
.nav a{color:var(--white);font-size:14px;font-weight:700;text-decoration:none;padding:0 21px;height:36px;display:flex;align-items:center;letter-spacing:.2px;white-space:nowrap}
.nav a.active{background:var(--blue)}
.social{display:flex;gap:22px}
.social span{width:17px;height:17px;border-radius:50%;background:currentColor;display:block}
.hero .social{left:765px;top:44px;color:var(--white)}
.hero .donate-top{left:962px;top:28px;width:163px;height:48px;font-size:19px}
.hero h1{left:75px;top:325px;font-size:62px;font-weight:900;line-height:64px;color:var(--white);text-transform:uppercase;white-space:nowrap}
.hero p{left:75px;top:458px;width:620px;font-size:25px;line-height:35px;color:var(--white);font-weight:700}
.hero .hero-read{left:75px;top:551px;width:220px;height:66px}
/* feature rows */
.feature{height:720px}
.feature .photo{left:75px;top:0;width:600px;height:577px}
.feature .panel{left:496px;top:119px;width:640px;height:460px;background:var(--white)}
.eyebrow{font-size:21px;font-weight:900;color:var(--blue);text-transform:uppercase}
.panel .eyebrow{left:28px;top:55px}
.panel h2{position:absolute;left:28px;top:78px;font-size:52px;font-weight:900;color:var(--ink);text-transform:uppercase}
.panel p{position:absolute;left:28px;top:148px;width:600px;font-size:15.6px;line-height:31.5px;color:var(--body)}
.panel .btn{left:28px;top:330px;width:220px;height:68px}
.overview{top:843px}
.overview .photo{background:linear-gradient(180deg,#b9a99a 0%,#6f6a6a 40%,#3a3536 70%,#8a7a72 100%)}
.services-row{top:2090px}
.services-row .photo{background:linear-gradient(135deg,#c5d8d4 0%,#b2c8c4 45%,#e3a79d 70%,#4a4340 100%)}
/* orange band */
.ways{top:1505px;height:503px;background:var(--orange)}
.way{position:absolute;top:118px;width:340px;text-align:center;color:var(--white)}
.way .icon{width:108px;height:108px;border:2px solid var(--yellow);margin:0 auto;display:flex;align-items:center;justify-content:center}
.way h3{font-size:28px;font-weight:900;margin-top:28px}
.way p{font-size:16px;line-height:30px;margin:12px auto 0;width:330px;color:#fde3d2}
/* impact */
.impact{top:2755px;height:540px;background:linear-gradient(90deg,#c89a7c 0%,#9f7f6b 40%,#6b4a3a 65%,#c7a28a 100%)}
.impact .box{left:75px;top:75px;width:527px;height:392px;background:var(--purple);text-align:center}
.impact h2{margin-top:42px;font-size:58px;line-height:67px;font-weight:900;color:var(--white)}
.impact .btn{left:152px;top:274px;width:220px;height:69px}
/* news */
.news{top:3330px;height:650px}
.news-head{width:1200px;text-align:center;top:18px}
.news-head h2{font-size:52px;font-weight:900;color:var(--ink);text-transform:uppercase;margin-top:2px}
.card{position:absolute;top:129px;width:331px}
.card .photo{position:relative;height:240px}
.date{position:absolute;left:0;bottom:0;width:76px;height:84px;background:var(--blue);color:var(--white);text-align:center;font-weight:700}
.date .m{font-size:21px;display:block;padding-top:6px}
.date .d{font-size:40px;font-weight:900;line-height:40px;display:block}
.card h3{font-size:22px;font-weight:900;color:var(--ink);margin-top:24px;white-space:nowrap}
.card p{font-size:15px;line-height:28px;margin-top:8px;color:var(--body)}
.outline{display:flex;align-items:center;justify-content:center;width:165px;height:52px;border:2px solid #f8d88a;color:var(--yellow);font-size:16px;margin-top:20px}
/* footer */
.site-footer{top:3980px;height:485px;background:var(--footer);color:var(--footer-text)}
.col{position:absolute;top:72px}
.col h4{font-size:24px;font-weight:700;color:var(--white);margin-bottom:12px;white-space:nowrap}
.col p,.col li{font-size:15.5px;line-height:30px;list-style:none}
.email{width:241px;height:50px;background:var(--white);color:var(--ink);font-size:15px;display:flex;align-items:center;padding-left:16px;margin-top:18px}
.subscribe{width:241px;height:50px;background:var(--yellow);color:var(--white);font-size:19px;font-weight:700;display:flex;align-items:center;justify-content:center;margin-top:16px}
.rule{left:75px;top:385px;width:1050px;height:1px;background:#3a3a3a}
.copy{left:75px;top:412px;font-size:13.5px;line-height:26px}
.site-footer .social{left:955px;top:428px;color:var(--white)}
</style>
</head>
<body>

<header class="hero">
  <div class="photo" role="img" aria-label="Masked student sitting at a classroom desk looking back over his shoulder" style="inset:0"></div>
  <div class="abs brand">Kelden Foundation</div>
  <nav class="abs nav">
    <a class="active">HOME</a><a>ABOUT US</a><a>SERVICES</a><a>LATEST NEWS</a><a>RESOURCES</a><a>CONTACT US</a>
  </nav>
  <div class="abs social"><span></span><span></span><span></span><span></span><span></span></div>
  <a class="btn donate-top">Donate Now</a>
  <h1 class="abs">Welcome to<br>Kelden Foundation</h1>
  <p class="abs">Sed ut perspiciatis unde omnis iste natus error sit voluptatem accusantium  doloremque.</p>
  <a class="btn btn-lg hero-read">Read More</a>
</header>

<section class="feature overview">
  <div class="photo" role="img" aria-label="Group of scholarship students posing on building steps"></div>
  <div class="abs panel">
    <div class="abs eyebrow">Who we are</div>
    <h2>Overview!</h2>
    <p>The Kelden Foundation was founded from Martin and Claire Hollis' vision to design an innovative program that would dramatically increase the graduation rates of first-generation college students—those who are first in their family to attend college. For several years prior to starting the foundation, the Hollises endowed scholarships at Lakeshore State University (LSU) ..</p>
    <a class="btn btn-lg">Read More</a>
  </div>
</section>

<section class="ways">
  <div class="way" style="left:70px">
    <div class="icon"><svg width="64" height="64" viewBox="0 0 64 64" fill="none" stroke="#fff" stroke-width="2"><rect x="6" y="8" width="30" height="24"/><rect x="26" y="28" width="32" height="26"/><path d="M12 16h18M12 22h12M34 36h18M34 42h12"/></svg></div>
    <h3>Media</h3>
    <p>Sed ut perspiciatis unde omnis iste natus error sit voluptatem accusantium doloremque laudantium.</p>
  </div>
  <div class="way" style="left:430px">
    <div class="icon"><svg width="64" height="64" viewBox="0 0 64 64" fill="none" stroke="#fff" stroke-width="2"><circle cx="22" cy="20" r="7"/><circle cx="42" cy="20" r="7"/><path d="M8 44c0-8 6-13 14-13s14 5 14 13M28 44c0-8 6-13 14-13s14 5 14 13"/><path d="M10 52h44"/></svg></div>
    <h3>Become Volunteer</h3>
    <p>Sed ut perspiciatis unde omnis iste natus error sit voluptatem accusantium doloremque laudantium.</p>
  </div>
  <div class="way" style="left:791px">
    <div class="icon"><svg width="64" height="64" viewBox="0 0 64 64" fill="none" stroke="#fff" stroke-width="2"><path d="M10 30l22-10 22 10-22 12z"/><path d="M10 30v14l22 12 22-12V30"/><path d="M32 42v14"/><path d="M32 18c-4-6-12-2-8 4l8 6 8-6c4-6-4-10-8-4z"/></svg></div>
    <h3>Send Donation</h3>
    <p>Sed ut perspiciatis unde omnis iste natus error sit voluptatem accusantium doloremque laudantium.</p>
  </div>
</section>

<section class="feature services-row">
  <div class="photo" role="img" aria-label="Piggy bank wearing a graduation cap with a tassel"></div>
  <div class="abs panel">
    <div class="abs eyebrow">Our services</div>
    <h2>What we do</h2>
    <p>Sed ut perspiciatis unde omnis iste natus error sit voluptatem accusantium doloremque laudantium, totam rem aperiam, eaque ipsa quae ab illo inventore veritatis et quasi architecto beatae vitae dicta sunt explicaboenim ipsam voluptatem quia voluptas sit aspernatur aut odit aut fugit, sed quia consequuntur.</p>
    <a class="btn btn-lg">Read More</a>
  </div>
</section>

<section class="impact">
  <div class="photo" role="img" aria-label="Children stacking their hands together in a circle" style="inset:0"></div>
  <div class="abs box">
    <h2>Over 23 Million<br>Children get<br>Benefit</h2>
    <a class="btn btn-lg">Donate Now</a>
  </div>
</section>

<section class="news">
  <div class="abs news-head">
    <div class="eyebrow">What's new</div>
    <h2>Latest News</h2>
  </div>
  <article class="card" style="left:75px">
    <div class="photo" role="img" aria-label="Student holding a folder" style="background:linear-gradient(135deg,#6b3a26,#3c2418 60%,#d9d2c8)"><div class="date"><span class="m">Aug</span><span class="d">28</span></div></div>
    <h3>Sed ut perspiciatis unde omnis</h3>
    <p>Nemo enim ipsam voluptatem quia voluptas sit aspernatur aut odit aut fugit, sed quia consequuntur magni.</p>
    <div class="outline">Read More</div>
  </article>
  <article class="card" style="left:435px">
    <div class="photo" role="img" aria-label="Child writing in a notebook outdoors" style="background:linear-gradient(135deg,#8fa6a3,#b49a7a 50%,#5f6a5e)"><div class="date"><span class="m">Aug</span><span class="d">28</span></div></div>
    <h3>Sed ut perspiciatis unde omnis</h3>
    <p>Nemo enim ipsam voluptatem quia voluptas sit aspernatur aut odit aut fugit, sed quia consequuntur magni.</p>
    <div class="outline">Read More</div>
  </article>
  <article class="card" style="left:796px">
    <div class="photo" role="img" aria-label="Students studying together in a park" style="background:linear-gradient(135deg,#6f8f4a,#3f5a86 50%,#b23a3a)"><div class="date"><span class="m">Aug</span><span class="d">28</span></div></div>
    <h3>Sed ut perspiciatis unde omnis</h3>
    <p>Nemo enim ipsam voluptatem quia voluptas sit aspernatur aut odit aut fugit, sed quia consequuntur magni.</p>
    <div class="outline">Read More</div>
  </article>
</section>

<footer class="site-footer">
  <div class="col" style="left:75px;width:290px">
    <h4>Kelden Foundation</h4>
    <p>Lorem ipsum dolor sit amet, consectetur adipiscing elit, sed do eiusmod tempor  incididunt ut labore et dolore magna aliqua. Ut enim ad minim veniam, quis  nostrud exerc itation ullamco laboris nisi ut aliquip ex ea commodo.</p>
  </div>
  <div class="col" style="left:435px">
    <h4>Site Map</h4>
    <ul><li>Home</li><li>About Us</li><li>Services</li><li>Latest News</li><li>Resources</li><li>Contact Us</li></ul>
  </div>
  <div class="col" style="left:635px">
    <h4>Resources</h4>
    <ul><li>et dolore magna aliqua</li><li>Enim ad minim</li><li>Quis nostrud exercitation</li><li>Ullamco laboris nisi</li><li>Aliquipmmodo</li></ul>
  </div>
  <div class="col" style="left:884px;width:241px">
    <h4>Newsletter Signup</h4>
    <p style="line-height:22px">Lorem ipsum dolor sit amet, co nsectetur adipiscing</p>
    <div class="email">Email Address</div>
    <div class="subscribe">Subscribe</div>
  </div>
  <div class="abs rule"></div>
  <div class="abs copy">Copyright © 2021 Company Name<br>All Right Reserved</div>
  <div class="abs social"><span></span><span></span><span></span><span></span><span></span></div>
</footer>

</body>
</html>
```